Flyer-Design für Ofenservice Firma
Zielgruppe
Die Firma hat als Kerngeschäft Wartung, Reinigung, Reparatur und Inbetriebnahme von Öfen und Kaminen aller Art. Der Fokus liegt dabei auf Pelletöfen. Die Firma versteht sich als zuverlässiger Dienstleister mit gutem Preisleistungsverhältnis. Zielgruppe sind hauptsächlich private Bewohner von Einfamilienhäusern in der ländlichen Gegend (Hessen)
Aufgabenstellung
Zur Bekanntmachung nach Neugründung soll ein Faltflyer gestaltet werden mit insgesamt 6 Bereichen. Die Informationen, welche auf den Flyer sollen, entnehmen Sie bitte dem Entwurf (flyer.pdf). Dieser stellt nur eine erste Idee dar und darf gerne nach Belieben verändert bzw. neu gestaltet werden. Die enthaltenen Informationen, sollten im Großen und Ganzen aber beibehalten werden. Schön wäre evtl. auch eine Hervorhebung der Preise, da wir Preisführer im Markt sind. Auch die Bilder unseres Teams sollen in den Flyer integriert sein. Auf Anfrage kann ich auch gerne weitere Kamin- und Ofenfotos zur Verfügung stellen, für welche ich die Nutzungsrechte habe. Falls Sie weitere Informationen benötigen oder Fragen haben, kommen Sie gerne auf mich zu. Die Bilder dürfen gerne etwas ausgeschnitten werden. Es geht in erster Linie darum, dass die Kunden erkennen, welche Art von Ofen sie zu Hause haben.

```html
<!DOCTYPE html>
<html lang="de">
<head>
<meta charset="utf-8">
<title>FLAMWERK Ofenservice – Faltflyer</title>
<link href="https://fonts.googleapis.com/css2?family=Open+Sans:wght@400;600;700&display=swap" rel="stylesheet">
<style>
  :root {
    --slate: #5a626b;
    --slate-dark: #4a5159;
    --ink: #3f454c;
    --text: #4d535a;
    --orange: #c8661f;
    --white: #ffffff;
    --paper: #f4f4f4;
    --bg: #ebebeb;
  }
  * { margin: 0; padding: 0; box-sizing: border-box; }
  html, body { width: 1200px; height: 848px; overflow: hidden; background: var(--bg); }
  body { font-family: "Open Sans", Arial, sans-serif; position: relative; }

  .flyer {
    position: absolute; left: 118px; top: 75px; width: 980px; height: 698px;
    background: var(--slate); display: flex;
  }
  .panel { position: relative; height: 100%; }

  /* Left panel */
  .panel--intro { width: 323px; }
  .intro-sheet {
    position: absolute; left: 0; top: 25px; width: 323px; height: 673px;
    background: linear-gradient(180deg, var(--paper), var(--white) 60%);
  }
  .intro-brand { position: absolute; left: 30px; top: 38px; font-size: 18px; color: var(--ink); }
  .intro-brand b { font-weight: 700; }
  .intro-brand span { font-weight: 400; font-size: 15px; color: #7a8088; }
  .intro-claim { position: absolute; left: 30px; top: 62px; width: 275px; font-size: 15.5px; line-height: 20px; color: var(--ink); }
  .intro-copy { position: absolute; left: 30px; top: 128px; width: 270px; font-size: 11px; line-height: 14px; color: var(--text); text-align: justify; }
  .intro-copy p { margin-bottom: 14px; }
  .intro-copy strong { font-weight: 700; color: var(--ink); }
  .team-photo {
    position: absolute; left: 0; bottom: 0; width: 323px; height: 275px;
    background: linear-gradient(160deg, #d9d9d9 0%, #3a3a3a 55%, #1e1e1e 100%);
    clip-path: polygon(0 60px, 323px 0, 323px 275px, 0 275px);
  }

  /* Middle panel */
  .panel--services { width: 322px; color: var(--white); text-align: center; }
  .services-brand { position: absolute; top: 58px; width: 100%; font-size: 22px; font-weight: 700; letter-spacing: .5px; }
  .services-sub { position: absolute; top: 84px; width: 100%; font-size: 14px; }
  .services-list { position: absolute; top: 120px; left: 20px; width: 282px; font-size: 11.5px; line-height: 16px; }
  .services-list h3 { font-size: 11.5px; font-weight: 700; margin-bottom: 18px; }
  .services-list p { margin-bottom: 16px; }
  .contact { position: absolute; top: 483px; width: 100%; font-size: 13px; line-height: 19px; font-weight: 600; }
  .contact p { margin-bottom: 18px; }

  /* Right panel */
  .panel--cover { width: 335px; background: var(--white); }
  .cover-brand { position: absolute; top: 82px; width: 100%; text-align: center; font-size: 26px; font-weight: 700; letter-spacing: 2px; color: var(--slate); }
  .cover-brand-sub { position: absolute; top: 112px; left: 0; width: 100%; text-align: center; font-size: 13px; color: #8a9098; letter-spacing: 1px; padding-left: 90px; }
  .cover-art { position: absolute; left: 0; top: 0; }
  .cover-headline { position: absolute; left: 34px; top: 562px; font-size: 21px; line-height: 29px; font-weight: 700; color: var(--slate); text-transform: uppercase; letter-spacing: .3px; }
  .cover-url { position: absolute; left: 34px; top: 651px; font-size: 13px; font-weight: 700; color: var(--orange); }
</style>
</head>
<body>
<main class="flyer">
  <section class="panel panel--intro">
    <div class="intro-sheet"></div>
    <div class="intro-brand"><b>FLAMWERK</b> <span>Ofenservice</span></div>
    <p class="intro-claim">Ihr kompetenter Servicespezialist für Öfen aller Art.</p>
    <div class="intro-copy">
      <p>Als Inhaber geführtes Unternehmen bieten wir <strong>professionelle Serviceleistungen rund um Öfen aller Art</strong> (Kaminöfen, Pelletöfen, Scheitholzöfen, Kachelöfen, offene Kamine, Grund- und Speicheröfen).</p>
      <p>Durch erfahrene Mitarbeiter, regelmäßigen Personalschulungen und <strong>Zusammenarbeit mit namhaften Herstellern</strong> können wir ihnen eine breite Palette an Dienstleistungen rund um Kaminöfen bieten.</p>
      <p><strong>Guter Service muss nicht teuer sein!</strong> Überzeugen Sie sich von unserem <strong>Preis-Leistungs-Verhältnis</strong> sowie unseren <strong>exklusiven Konditionen</strong> bei Abschluss eines Wartungsvertrags.</p>
    </div>
    <div class="team-photo" role="img" aria-label="Teamfoto: drei Mitarbeiter in dunkler Arbeitskleidung vor hellem Hintergrund"></div>
  </section>

  <section class="panel panel--services">
    <div class="services-brand">FLAMWERK</div>
    <div class="services-sub">Ofenservice</div>
    <div class="services-list">
      <h3>Weitere Leistungen:</h3>
      <p><strong>Reparatur und Instandsetzung:</strong> Funktioniert ihr Ofen nicht richtig, sind wir schnellstmöglich für Sie da und setzen ihren Ofen wieder instand.</p>
      <p><strong>Inbetriebnahme:</strong> Sie haben einen neuen Ofen erworben und möchten sich über die richtige Nutzung und Befeuerung informieren?</p>
      <p><strong>Kaufberatung:</strong> Sie planen eine Neuanschaffung und möchten sich vorab über Anschlussmöglichkeiten, Brennstoffarten und Modelle informieren?<br>Wir beraten Sie unabhängig und auf Ihre Bedürfnisse zugeschnitten.</p>
    </div>
    <div class="contact">
      <p>FLAMWERK OFENSERVICE<br>Birkenweg 12<br>35390 Talheim</p>
      <p>Telefon:<br>06400 / 123-45-67</p>
      <p>Online:<br>info@flamwerk-ofenservice.de<br>www.flamwerk-ofenservice.de</p>
    </div>
  </section>

  <section class="panel panel--cover">
    <div class="cover-brand">FLAMWERK</div>
    <div class="cover-brand-sub">Ofenservice</div>
    <svg class="cover-art" width="335" height="698" viewBox="0 0 335 698">
      <defs>
        <linearGradient id="fireplaceTones" x1="0" y1="0" x2="1" y2="1">
          <stop offset="0" stop-color="#3a4350"/>
          <stop offset=".45" stop-color="#c9822e"/>
          <stop offset=".6" stop-color="#4a3a2c"/>
          <stop offset="1" stop-color="#1f1f22"/>
        </linearGradient>
      </defs>
      <polygon points="0,182 335,137 335,162 0,188" fill="var(--orange)"/>
      <polygon points="0,188 335,160 335,470 0,500" fill="url(#fireplaceTones)" role="img" aria-label="Foto eines modernen Eckkamins mit brennendem Feuer in einem Wohnraum"/>
      <polygon points="0,500 335,470 335,480 0,522" fill="var(--orange)"/>
    </svg>
    <div class="cover-headline">Ihr kompetenter<br>Servicespezialist<br>für Öfen aller Art</div>
    <div class="cover-url">www.flamwerk-ofenservice.de</div>
  </section>
</main>
</body>
</html>
```